COBALT YARDS needs bisness cards pronto

Bisness name is "COBALT YARDS" new bisness the bisness includes lawn mowing, garden matanace, and any jobs around the house.
I need a card that is colorful and vibrant and the bisness of lawn mowing maybe with some nature with it. It also needs my contact details"Desmond Larkwell mobile 0412563049 call for free quote and email gwen.brookvale@fernmail.com and a catchy tag line

Requirements
Must have
• Bisness name "COBALT YARDS"
Contact details "0412563049"
Email gwen.brookvale@fernmail.com
Call for free quote

```html
<!DOCTYPE html>
<html lang="en">
<head>
<meta charset="utf-8">
<title>COBALT YARDS – Business Cards</title>
<link rel="stylesheet" href="https://fonts.googleapis.com/css2?family=Ubuntu:wght@400;500;700&display=swap">
<style>
  :root {
    --backdrop: #6f8389;
    --card: #ffffff;
    --ink-dark: #3b3b3d;
    --ink-body: #4a4a4c;
    --brand-green: #3ea648;
    --grass-deep: #4f9a2a;
    --grass-mid: #79c23b;
    --grass-light: #b6e27a;
    --white: #ffffff;
  }
  * { box-sizing: border-box; margin: 0; padding: 0; }
  html, body {
    width: 1200px; height: 960px; overflow: hidden;
    background: var(--backdrop);
    font-family: "Ubuntu", sans-serif;
  }
  .canvas { position: relative; width: 1200px; height: 960px; }

  .card {
    position: absolute; left: 260px;
    width: 680px; height: 389px;
    background: var(--card);
    border-radius: 4px;
    box-shadow: 0 14px 30px rgba(0,0,0,0.28);
    overflow: hidden;
  }
  .card--front { top: 76px; }
  .card--back  { top: 505px; }

  .wordmark {
    position: absolute;
    font-family: "Ubuntu", sans-serif;
    font-weight: 700;
    color: var(--ink-dark);
    letter-spacing: 2px;
    white-space: nowrap;
  }
  .card--front .wordmark { left: 40px; top: 48px; font-size: 66px; }
  .card--back .wordmark  { left: 44px; top: 30px; font-size: 40px; }

  .holder-name {
    position: absolute; left: 250px; top: 178px;
    font-size: 28px; font-weight: 500;
    color: var(--ink-dark); letter-spacing: 0.5px;
  }
  .contact-list { position: absolute; left: 250px; top: 236px; list-style: none; }
  .contact-item {
    display: flex; align-items: center; gap: 16px;
    height: 46px; margin-bottom: 18px;
    font-size: 24px; color: var(--ink-body);
  }
  .contact-icon { width: 44px; height: 44px; flex: none; }

  .grass-field {
    position: absolute; left: 0; right: 0; bottom: 0; height: 290px;
    background: linear-gradient(to bottom,
      rgba(182,226,122,0) 0%,
      var(--grass-light) 22%,
      var(--grass-mid) 55%,
      var(--grass-deep) 100%);
  }
  .quote-badge {
    position: absolute; left: 476px; top: 70px;
    width: 176px; height: 176px;
  }
  .quote-badge svg { position: absolute; inset: 0; width: 100%; height: 100%; }
  .quote-badge__text {
    position: absolute; inset: 0;
    display: flex; align-items: center; justify-content: center;
    text-align: center;
    color: var(--white); font-size: 24px; font-weight: 500; line-height: 1.05;
    transform: rotate(-12deg);
  }
</style>
</head>
<body>
<main class="canvas">

  <section class="card card--front" aria-label="Business card front">
    <div class="wordmark">COBALT YARDS</div>
    <h1 class="holder-name">DESMOND LARKWELL</h1>
    <ul class="contact-list">
      <li class="contact-item">
        <svg class="contact-icon" viewBox="0 0 44 44" aria-hidden="true">
          <circle cx="22" cy="22" r="22" fill="var(--brand-green)"/>
          <rect x="15" y="9" width="14" height="26" rx="2" fill="var(--white)"/>
          <rect x="17.5" y="12" width="9" height="7" fill="var(--brand-green)"/>
          <g fill="var(--brand-green)">
            <rect x="17.5" y="22" width="2.5" height="2.5"/><rect x="20.8" y="22" width="2.5" height="2.5"/><rect x="24" y="22" width="2.5" height="2.5"/>
            <rect x="17.5" y="26" width="2.5" height="2.5"/><rect x="20.8" y="26" width="2.5" height="2.5"/><rect x="24" y="26" width="2.5" height="2.5"/>
            <rect x="17.5" y="30" width="2.5" height="2.5"/><rect x="20.8" y="30" width="2.5" height="2.5"/><rect x="24" y="30" width="2.5" height="2.5"/>
          </g>
        </svg>
        <span>0412563049</span>
      </li>
      <li class="contact-item">
        <svg class="contact-icon" viewBox="0 0 44 44" aria-hidden="true">
          <circle cx="22" cy="22" r="22" fill="var(--brand-green)"/>
          <rect x="10" y="13" width="24" height="18" fill="none" stroke="var(--white)" stroke-width="2"/>
          <polyline points="10,13 22,24 34,13" fill="none" stroke="var(--white)" stroke-width="2"/>
          <polyline points="10,31 19,22 M25,22 34,31" fill="none" stroke="var(--white)" stroke-width="2"/>
          <line x1="25" y1="22" x2="34" y2="31" stroke="var(--white)" stroke-width="2"/>
        </svg>
        <span>gwen.brookvale@fernmail.com</span>
      </li>
    </ul>
  </section>

  <section class="card card--back" aria-label="Business card back">
    <div class="grass-field" role="img" aria-label="Close-up photograph of fresh green lawn grass"></div>
    <div class="wordmark">COBALT YARDS</div>
    <div class="quote-badge">
      <svg viewBox="0 0 100 100" aria-hidden="true">
        <polygon fill="var(--brand-green)" points="100,50 91.5,61.1 93.3,75 80.4,80.4 75,93.3 61.1,91.5 50,100 38.9,91.5 25,93.3 19.6,80.4 6.7,75 8.5,61.1 0,50 8.5,38.9 6.7,25 19.6,19.6 25,6.7 38.9,8.5 50,0 61.1,8.5 75,6.7 80.4,19.6 93.3,25 91.5,38.9"/>
      </svg>
      <p class="quote-badge__text">Call<br>for free<br>quote</p>
    </div>
  </section>

</main>
</body>
</html>
```